Business Card Design for boarding house accomodation business

I need a business card design for my Sydney based boarding house business accomodation. providing rooms for rent in Sydney Australia with shard bathroom and kitchen.
The front of card, are my details with details of head office and the rear of card to have details of locations providing rooms for rent.

Industry/Entity Type

Business

Contact Information for Business Card

Front of card details:
HOLLINBROOK MANAGEMENT PTY LTD t/a
CALLOWAY'S GUEST HOUSE
ABN:52930718264
Daniel Vukasinov
48 Pembury st
Newtown 2042
Mobile:0412876390
Email:daniel@callowaysguesthouse-example.com.au

Back of Card:
Locations:
-48 Pembury st
Newtown 2042

-392 Carvel st
Erskineville 2043

-87 Whitlam st
Bondi 2026

-264 Ashcombe rd
Marrickville 2043

```html
<!DOCTYPE html>
<html lang="en">
<head>
<meta charset="utf-8">
<title>Hollinbrook Management – Business Card</title>
<link rel="stylesheet" href="https://fonts.googleapis.com/css2?family=Open+Sans:wght@400;600;700&display=swap">
<style>
  :root {
    --page-bg: #e9e9e6;
    --card-white: #ffffff;
    --card-black: #111111;
    --green-light: #7cc242;
    --green-dark: #1f8b45;
    --green-name: #3aa048;
    --ink: #222222;
    --white: #ffffff;
  }
  * { box-sizing: border-box; margin: 0; padding: 0; }
  html, body {
    width: 1200px; height: 900px; overflow: hidden;
    background: var(--page-bg);
    font-family: "Open Sans", Arial, sans-serif;
  }
  .canvas {
    width: 1200px; height: 900px;
    display: flex; align-items: center; justify-content: center; gap: 40px;
  }
  .card {
    position: relative;
    width: 540px; height: 309px;
    overflow: hidden;
    box-shadow: 0 6px 18px rgba(0,0,0,.18);
  }
  .card-front { background: var(--card-white); color: var(--ink); }
  .card-back  { background: var(--card-black); color: var(--white); }

  .card-shapes { position: absolute; inset: 0; width: 100%; height: 100%; }

  .holder-name {
    position: absolute; left: 62px; top: 26px;
    font-size: 21px; font-weight: 600; color: var(--green-name);
  }
  .holder-name .surname { color: var(--green-dark); }

  .contact-list {
    position: absolute; left: 40px; top: 122px;
    list-style: none; font-size: 12.5px; line-height: 19px; color: var(--ink);
  }
  .contact-list li { display: flex; align-items: center; gap: 6px; white-space: nowrap; }
  .contact-list .label { color: var(--green-dark); font-weight: 700; }
  .contact-list svg { width: 11px; height: 11px; fill: var(--green-dark); flex: none; }

  .brand {
    position: absolute; right: 24px;
    display: flex; flex-direction: column; align-items: center; gap: 5px;
    text-align: center;
  }
  .card-front .brand { top: 68px; }
  .card-back .brand  { top: 40px; }
  .brand-dot { width: 34px; height: 34px; border-radius: 50%; flex: none; }
  .card-front .brand-dot { background: var(--green-light); }
  .card-back .brand-dot  { background: var(--white); }
  .brand-name {
    font-size: 12.5px; font-weight: 700; line-height: 16px; letter-spacing: .3px;
    white-space: nowrap;
  }
  .card-front .brand-name { color: var(--ink); }
  .card-back .brand-name  { color: var(--white); }
  .brand-name span { display: block; font-size: 9.5px; letter-spacing: 1.2px; }

  .locations { position: absolute; left: 34px; top: 56px; }
  .locations h2 { font-size: 17px; font-weight: 700; margin-bottom: 8px; }
  .locations ul { list-style: none; font-size: 12.5px; line-height: 22px; }
</style>
</head>
<body>
<main class="canvas">

  <section class="card card-front" aria-label="Card front">
    <svg class="card-shapes" viewBox="0 0 540 309" aria-hidden="true">
      <polygon points="0,12 36,12 12,52 0,52" fill="var(--green-light)"/>
      <polygon points="36,12 46,12 46,52 12,52" fill="var(--green-dark)"/>
      <polygon points="0,230 240,230 262,262 0,262" fill="var(--green-light)"/>
      <polygon points="250,268 540,268 540,309 276,309" fill="var(--green-dark)"/>
    </svg>

    <h1 class="holder-name">Daniel <span class="surname">Vukasinov</span></h1>

    <div class="brand">
      <span class="brand-dot"></span>
      <p class="brand-name">HOLLINBROOK MANAGEMENT PTY LTD<span>CALLOWAY'S GUEST HOUSE</span></p>
    </div>

    <ul class="contact-list">
      <li><span class="label">ABN:</span> 52930718264</li>
      <li>
        <svg viewBox="0 0 24 24" aria-hidden="true"><path d="M6.6 10.8a15.1 15.1 0 0 0 6.6 6.6l2.2-2.2a1 1 0 0 1 1-.25 11.4 11.4 0 0 0 3.6.57 1 1 0 0 1 1 1V20a1 1 0 0 1-1 1A17 17 0 0 1 3 4a1 1 0 0 1 1-1h3.5a1 1 0 0 1 1 1c0 1.25.2 2.450.57 3.57a1 1 0 0 1-.25 1z"/></svg>
        0412876390
      </li>
      <li>
        <svg viewBox="0 0 24 24" aria-hidden="true"><path d="M2 5h20v14H2z" fill="var(--green-dark)"/><path d="M2 5l10 8 10-8" fill="none" stroke="#fff" stroke-width="1.6"/></svg>
        daniel@callowaysguesthouse-example.com.au
      </li>
      <li>48 Pembury st Newtown 2042</li>
    </ul>
  </section>

  <section class="card card-back" aria-label="Card back">
    <div class="locations">
      <h2>Locations</h2>
      <ul>
        <li>48 Pembury st Newtown 2042</li>
        <li>392 Carvel st Erskineville 2043</li>
        <li>87 Whitlam st Bondi 2026</li>
        <li>264 Ashcombe rd Marrickville 2043</li>
      </ul>
    </div>

    <div class="brand">
      <span class="brand-dot"></span>
      <p class="brand-name">HOLLINBROOK MANAGEMENT PTY LTD<span>CALLOWAY'S GUEST HOUSE</span></p>
    </div>
  </section>

</main>
</body>
</html>
```